THE BRIGHT KITE SITTER - Temporary, On The Spot , Child Minding and Dog Walking Service

I am THE BRIGHT KITE SITTER. I am available for temporary on-the-spot bookings, for those times when parents need 1 or 2 hours to duck out to the supermarket but they can' t because their baby is taking a nap. Or maybe they have a 1 to 2 hour appointment where they can't take the kids and have no one to look after them. Or they may be they are at a luncheon and have to reluctantly tear themselves away to pick up the kids from school.
This is where I come to the rescue.
I can be hired for a minimum of 1 hour, or a maximum of 2 hours. I will come to them. Daytime and Evening rates apply. Maximum 3 children at one time.
I will entertain the children, do the odd job around the house, make delicious snacks and I can pickup children from school when necessary. I am also available to walk your beloved dog.
The Bright Kite Sitter is like no other nanny you will ever have - fun, reliable, super-tidy , and comes with impeccable references. Your life will become a whole lot easier with me in it!

I'd like a flyer that looks 'classy' as well as eye-catching. I'm 51 years old, but a 'very young' 51 so I'm also looking for a modern flyer.

Target Market(s)

Busy Mums and Dads and Guardians.

Industry/Entity Type

It Service

Requirements
Must have
• Maximum of 3 children at any 1 time.
Should not have
• Nasty pets!

```html
<!DOCTYPE html>
<html lang="en">
<head>
<meta charset="utf-8">
<title>The Bright Kite Sitter – Flyer</title>
<link rel="stylesheet" href="https://fonts.googleapis.com/css2?family=Varela+Round&family=Quicksand:wght@700&family=Arimo:wght@400;700&display=swap">
<style>
  :root {
    --blush: #f8c9c8;
    --card: #ffffff;
    --frame-red: #e8373a;
    --gold: #f6b81f;
    --orange: #f07a2a;
    --red: #e8373a;
    --panel: #fdf0c2;
    --ink: #333333;
    --snack: #f7a823;
    --pickup: #3f9a45;
    --dog: #7a4a2e;
    --clown: #e8373a;
    --blue: #3b6fc4;
    --pink: #f4b3b2;
    --tab-text: #e2585a;
  }
  * { margin: 0; padding: 0; box-sizing: border-box; }
  html, body { width: 849px; height: 1200px; overflow: hidden; }
  body {
    background: var(--blush);
    font-family: "Varela Round", sans-serif;
    position: relative;
  }
  .flyer-card {
    position: absolute;
    left: 62px; top: 58px;
    width: 726px; height: 814px;
    background: var(--card);
    border: 6px dashed var(--frame-red);
    border-radius: 6px;
    padding: 52px 36px 0;
    text-align: center;
  }
  .brand {
    position: absolute;
    left: 50%; top: -30px;
    transform: translateX(-50%);
    display: flex; align-items: center; gap: 12px;
    background: var(--card);
    padding: 10px 22px;
    border-radius: 10px;
    white-space: nowrap;
  }
  .brand-dot { width: 30px; height: 30px; border-radius: 50%; background: var(--gold); }
  .brand-name { font-size: 28px; color: var(--red); letter-spacing: 1px; }
  .abn { color: var(--orange); font-size: 25px; letter-spacing: 1px; }
  .intro { margin-top: 8px; color: var(--orange); font-size: 27px; line-height: 1.2; }
  .intro strong { color: var(--red); font-family: "Quicksand", sans-serif; font-weight: 700; }
  .pitch { margin: 14px auto 0; width: 620px; color: var(--red); font-size: 22px; line-height: 1.25; }
  .services {
    margin: 18px auto 0;
    width: 640px; height: 236px;
    background: var(--panel); border-radius: 12px;
  }
  .services h2 { font-weight: 400; font-size: 26px; color: var(--ink); padding-top: 12px; }
  .service-list { display: flex; justify-content: space-around; margin-top: 14px; list-style: none; }
  .service { width: 140px; font-size: 20px; line-height: 1.15; }
  .service-icon { width: 92px; height: 92px; border-radius: 18px; margin: 0 auto 8px; }
  .snack { color: var(--snack); } .snack .service-icon { background: var(--snack); }
  .pickup { color: var(--pickup); } .pickup .service-icon { background: var(--pickup); }
  .dog { color: var(--dog); } .dog .service-icon { background: var(--dog); }
  .clown { color: var(--clown); } .clown .service-icon { background: var(--clown); }
  .details {
    display: flex; justify-content: center; gap: 90px;
    margin-top: 20px;
    font-family: "Arimo", sans-serif; color: var(--ink);
  }
  .hours, .capacity { width: 180px; font-size: 16px; line-height: 1.25; }
  .hours-badge { display: block; width: 80px; height: 46px; margin: 0 auto 6px; }
  .capacity { font-size: 17px; }
  .capacity-art {
    width: 90px; height: 50px; margin: 0 auto 8px; border-radius: 25px;
    background: linear-gradient(90deg, #f2c36b, #e9a07a, #f2c36b);
  }
  .travel-note {
    margin: 20px auto 0; width: 600px;
    font-family: "Arimo", sans-serif; font-size: 14px; color: var(--ink); line-height: 1.3;
  }
  .tear-tabs {
    position: absolute; left: 0; top: 900px; width: 849px; height: 300px;
    display: flex; border-top: 2px dashed #fff;
  }
  .tab {
    flex: 1; border-right: 2px dashed #fff;
    display: flex; justify-content: center; align-items: center;
  }
  .tab:last-child { border-right: none; }
  .tab p {
    writing-mode: vertical-rl; transform: rotate(180deg);
    font-family: "Arimo", sans-serif; font-size: 14px; line-height: 1.2;
    color: var(--tab-text); white-space: nowrap;
  }
</style>
</head>
<body>
  <main class="flyer-card">
    <div class="brand">
      <span class="brand-dot"></span>
      <span class="brand-name">THE BRIGHT KITE SITTER</span>
    </div>

    <p class="abn">ABN: 12 345 678 901</p>
    <p class="intro">Take a short break. Nap or coffee time because <strong>THE BRIGHT KITE SITTER</strong> is here to look after your children.</p>
    <p class="pitch">The Bright Kite Sitter is like no other nanny you will ever have - fun, reliable, super-tidy , and comes with impeccable references. Your life will become a whole lot easier with me in it!</p>

    <section class="services">
      <h2>This is where I come to the rescue</h2>
      <ul class="service-list">
        <li class="service snack"><div class="service-icon" role="img" aria-label="Cupcake icon"></div>Make delicious snacks</li>
        <li class="service pickup"><div class="service-icon" role="img" aria-label="Graduation cap icon"></div>Pickup children</li>
        <li class="service dog"><div class="service-icon" role="img" aria-label="Dog icon"></div>Walk your dog</li>
        <li class="service clown"><div class="service-icon" role="img" aria-label="Entertainer icon"></div>Entertain children</li>
      </ul>
    </section>

    <section class="details">
      <div class="hours">
        <svg class="hours-badge" viewBox="0 0 80 46">
          <circle cx="22" cy="23" r="18" fill="var(--pink)"/>
          <text x="22" y="30" text-anchor="middle" font-family="Arimo, sans-serif" font-size="20" font-weight="700" fill="var(--red)">1</text>
          <line x1="38" y1="23" x2="44" y2="23" stroke="var(--ink)" stroke-width="3"/>
          <circle cx="58" cy="23" r="18" fill="var(--blue)"/>
          <text x="58" y="30" text-anchor="middle" font-family="Arimo, sans-serif" font-size="20" font-weight="700" fill="#fff">2</text>
        </svg>
        <p>Available for<br>Min. 1 Hour - $30.00<br>Max. 2 Hours - $55.00<br>Evening rates apply.</p>
      </div>
      <div class="capacity">
        <div class="capacity-art" role="img" aria-label="Illustration of three children"></div>
        <p>Maximum<br>3 children<br>at one time</p>
      </div>
    </section>

    <p class="travel-note">For areas over 10km and up to 20km from Maple Grove, an additional $10 fee applies on the overall hire rate.</p>
  </main>

  <div class="tear-tabs">
    <div class="tab"><p>THE BRIGHT KITE SITTER<br>0400 123 456</p></div>
    <div class="tab"><p>THE BRIGHT KITE SITTER<br>0400 123 456</p></div>
    <div class="tab"><p>THE BRIGHT KITE SITTER<br>0400 123 456</p></div>
    <div class="tab"><p>THE BRIGHT KITE SITTER<br>0400 123 456</p></div>
    <div class="tab"><p>THE BRIGHT KITE SITTER<br>0400 123 456</p></div>
    <div class="tab"><p>THE BRIGHT KITE SITTER<br>0400 123 456</p></div>
    <div class="tab"><p>THE BRIGHT KITE SITTER<br>0400 123 456</p></div>
    <div class="tab"><p>THE BRIGHT KITE SITTER<br>0400 123 456</p></div>
    <div class="tab"><p>THE BRIGHT KITE SITTER<br>0400 123 456</p></div>
    <div class="tab"><p>THE BRIGHT KITE SITTER<br>0400 123 456</p></div>
    <div class="tab"><p>THE BRIGHT KITE SITTER<br>0400 123 456</p></div>
    <div class="tab"><p>THE BRIGHT KITE SITTER<br>0400 123 456</p></div>
    <div class="tab"><p>THE BRIGHT KITE SITTER<br>0400 123 456</p></div>
    <div class="tab"><p>THE BRIGHT KITE SITTER<br>0400 123 456</p></div>
    <div class="tab"><p>THE BRIGHT KITE SITTER<br>0400 123 456</p></div>
    <div class="tab"><p>THE BRIGHT KITE SITTER<br>0400 123 456</p></div>
    <div class="tab"><p>THE BRIGHT KITE SITTER<br>0400 123 456</p></div>
    <div class="tab"><p>THE BRIGHT KITE SITTER<br>0400 123 456</p></div>
    <div class="tab"><p>THE BRIGHT KITE SITTER<br>0400 123 456</p></div>
  </div>
</body>
</html>
```